Help create our baby! Modern facial bar website.

We want a RESPONSIVE Wordpress website that is clean, gender neutral, and modern. Mobile first is the way to go. This must look awesome on a mobile device. We are opening a modern and fresh organic mask bar with modern decor. Think clean, fresh, airy. We will also offer other services. We will offer many of the services that movie stars have access to, such as Light Therapy, Oxygen Facial, Microcurrent, Microderm, etc. Think express facial bar that is results driven. Our niche is for busy men and women who want to see results, and don't have a lot of time to spend at a spa. We are not a traditional spa. So no walking around in robes. Our services are half the cost when compared to traditional spas.

We will offer a membership program with different tiers of memberships. This is something that we want to franchise if our location is successful.

We are not into a typical spa/massage website type design with lots of commonly used images of people getting massages and facials.

We are thinking of a white background, with pops of color that are the same as our logo.

Please include the following hex codes in the website (don't think these are exact...we'd like to match the provided logo):
ea8e05
9ca0a8
14c5d4

The font of our logo is Coolvetica RG.

Target Market(s)

Young, hip, busy professionals who want to take care of their skin. Men, women, teens. Metropolitan US city.

Industry/Entity Type

Skin Care Product

Coding

Coded - Design and coding required

Font styles to use
Sans Serif

Requirements
Must have
• Modern, clean, fresh website. White background with pops of color. We need to be able to edit the text and add services through Wordpress.
Nice to have
• Pictures of men and women having fun. Some could have creams and products on their face. We want to promote facial parties. SEO is very important to us, so please design with that in mind.
Should not have
• No clip art. No cheesy pictures of women getting massages and facials. We want to avoid looking like one of the many places that do "facials" but do not really specialize in skincare. We want to avoid looking like a Nail place, or foot spa place that also does facials (so...no butterflies, leaves, and flowers).

```html
<!DOCTYPE html>
<html lang="en">
<head>
<meta charset="utf-8">
<title>GlowLab – Facial Bar</title>
<link href="https://fonts.googleapis.com/css2?family=Archivo:wght@400;600;700&family=Open+Sans:ital,wght@0,400;0,600;1,400&display=swap" rel="stylesheet">
<style>
:root{
  --teal:#14c5d4;
  --teal-dark:#12b6c4;
  --orange:#ea8e05;
  --grey:#9ca0a8;
  --ink:#3d3d3d;
  --text:#555;
  --line:#e4e4e4;
  --hero:#b8bde3;
  --footer:#f4f4f4;
  --white:#fff;
}
*{box-sizing:border-box;margin:0;padding:0}
html,body{width:1200px;height:2525px;overflow:hidden}
body{position:relative;background:var(--white);font-family:"Open Sans",Arial,sans-serif;color:var(--text)}
.abs{position:absolute}
.head-font{font-family:"Archivo",Arial,sans-serif}

/* header */
.brand{position:absolute;left:98px;top:30px;font-family:"Archivo",Arial,sans-serif;font-weight:700;font-size:50px;color:var(--teal);letter-spacing:-1px;line-height:1}
.appt{position:absolute;left:792px;top:38px;font-family:"Archivo",Arial,sans-serif}
.appt .label{font-size:19px;color:var(--grey);font-weight:600}
.appt .phone{font-size:21px;color:var(--teal);margin-top:2px}
.btn{display:inline-block;background:var(--orange);color:var(--white);font-family:"Archivo",Arial,sans-serif;font-weight:600;text-transform:uppercase;text-align:center;border-radius:2px}
.book{position:absolute;left:998px;top:45px;width:104px;height:38px;line-height:38px;font-size:14px}

/* nav */
.nav{position:absolute;left:0;top:123px;width:1200px;height:52px;background:var(--teal);display:flex;padding-left:98px}
.nav a{color:var(--white);text-decoration:none;font-family:"Archivo",Arial,sans-serif;font-weight:600;font-size:13.5px;line-height:52px;padding:0 29px;border-right:1px solid rgba(255,255,255,.25)}
.nav a.active{background:var(--orange);padding:0 30px}

/* hero */
.hero{position:absolute;left:0;top:175px;width:1200px;height:520px;background:linear-gradient(90deg,#c9cbe9,var(--hero) 60%,#b3b8e0)}
.hero-photo{position:absolute;left:0;top:0;width:623px;height:520px;background:radial-gradient(ellipse at 40% 50%,#c9b2a4 0%,#b79f93 35%,rgba(184,189,227,0) 72%)}
.hero h1{position:absolute;left:729px;top:312px;font-family:"Archivo",Arial,sans-serif;font-weight:700;font-size:50px;color:var(--ink);line-height:1}
.hero h2{position:absolute;left:729px;top:372px;font-family:"Archivo",Arial,sans-serif;font-weight:700;font-size:28px;color:var(--ink)}
.hero p{position:absolute;left:733px;top:412px;width:380px;font-size:14.5px;line-height:23px;color:#444}
.hero .more{position:absolute;left:733px;top:478px;width:180px;height:40px;line-height:40px;font-size:14px}
.dots{position:absolute;left:737px;top:538px;display:flex;gap:8px;align-items:center}
.dots i{width:10px;height:10px;border-radius:50%;background:#444}
.dots i.on{width:16px;height:16px;background:var(--white);border:3px solid #c9cbe9;box-shadow:0 0 0 1px #999}

/* section titles */
.sec-title{position:absolute;left:0;width:1200px;text-align:center;font-family:"Archivo",Arial,sans-serif;font-weight:700;font-size:29px;color:var(--ink)}

/* services */
.service{position:absolute;top:875px;width:231px;height:253px;border:1px solid var(--line);background:var(--white);text-align:center}
.service .pic{position:absolute;left:42px;top:-52px;width:145px;height:145px;border-radius:50%;border:3px solid var(--teal);background:radial-gradient(circle at 45% 45%,#f1dfd6,#c7b9b4 60%,#8fa3b2)}
.service .shadow{position:absolute;left:55px;top:100px;width:120px;height:10px;border-radius:50%;background:radial-gradient(ellipse,rgba(0,0,0,.12),rgba(0,0,0,0) 70%)}
.service h3{position:absolute;top:138px;width:100%;font-family:"Archivo",Arial,sans-serif;font-weight:600;font-size:14px;color:#333}
.service p{position:absolute;top:163px;left:18px;width:195px;font-size:12px;line-height:20px;color:#555}
.service .arrow{position:absolute;left:108px;top:231px}

/* welcome */
.welcome{position:absolute;left:0;top:1188px;width:1200px;height:386px;background:linear-gradient(90deg,var(--teal) 0%,#21bfcd 50%,var(--teal) 100%)}
.welcome h2{position:absolute;top:92px;width:100%;text-align:center;font-family:"Archivo",Arial,sans-serif;font-weight:700;font-size:31px;color:var(--white)}
.welcome p{position:absolute;left:180px;width:840px;text-align:center;font-size:11.5px;line-height:22px;color:var(--white)}

/* membership */
.plan{position:absolute;top:1690px;width:306px;height:234px;border:1px solid var(--line);background:var(--white);text-align:center}
.plan .top{height:113px;background:var(--orange);color:var(--white);font-family:"Archivo",Arial,sans-serif;padding-top:24px}
.plan .name{font-size:22px;font-weight:700}
.plan .price{font-size:34px;font-weight:700;margin-top:4px;letter-spacing:-1px}
.plan .price small{font-size:16px}
.plan .price sup{font-size:15px}
.plan ul{list-style:none;margin-top:14px;font-size:12.5px;line-height:27px;color:#555}
.plan .read{position:absolute;left:107px;top:221px;width:92px;height:27px;line-height:27px;font-size:12px}

/* testimonial */
.testimonial{position:absolute;left:0;top:2011px;width:1200px;height:211px;background:var(--teal)}
.testimonial h2{position:absolute;left:97px;top:90px;font-family:"Archivo",Arial,sans-serif;font-weight:700;font-size:28px;color:var(--white);letter-spacing:-.5px}
.avatar{position:absolute;left:322px;top:45px;width:110px;height:110px;border-radius:50%;border:4px solid var(--white);background:radial-gradient(circle at 50% 45%,#f2d8c8,#c79b83 70%)}
.quote{position:absolute;left:475px;top:48px;width:625px;font-style:italic;font-size:12.5px;line-height:21px;color:var(--white)}
.author{position:absolute;left:475px;top:125px;font-style:italic;font-size:15px;color:var(--white)}
.arrows{position:absolute;left:472px;top:161px;display:flex;gap:3px}

/* footer */
.footer{position:absolute;left:0;top:2222px;width:1200px;height:252px;background:var(--footer)}
.footer .brand{left:100px;top:80px;font-size:46px}
.social{position:absolute;left:152px;top:141px;display:flex;gap:5px}
.social i{width:15px;height:15px;background:var(--orange);border-radius:2px}
.footer h4{position:absolute;top:38px;font-family:"Archivo",Arial,sans-serif;font-weight:700;font-size:15px;color:#333}
.links{position:absolute;left:371px;top:74px;list-style:none;font-size:11px;line-height:23px;color:#444}
.news-text{position:absolute;left:586px;top:66px;width:270px;font-size:11.5px;line-height:21px;color:#444}
.field{position:absolute;left:586px;width:262px;height:42px;background:var(--white);border:1px solid var(--line);font-size:11.5px;color:#333;line-height:40px;padding-left:14px}
.subscribe{position:absolute;left:750px;top:167px;width:98px;height:42px;line-height:42px;background:var(--teal);color:var(--white);font-size:13px;text-align:center}
.contact{position:absolute;left:936px;top:72px;font-size:13px;line-height:21px;color:#333}
.contact-row{position:absolute;left:936px;display:flex;align-items:center;gap:14px;font-size:14px;color:#333}

.bottom{position:absolute;left:0;top:2474px;width:1200px;height:51px;background:var(--teal);text-align:center;line-height:51px;font-size:11.5px;color:var(--white)}
</style>
</head>
<body>

<header>
  <div class="brand">glowlab</div>
  <div class="appt">
    <div class="label">Request Appointment</div>
    <div class="phone">(555) 014-2290</div>
  </div>
  <a class="btn book">Book Now</a>
</header>

<nav class="nav">
  <a class="active">HOME</a>
  <a>FACIAL MENU</a>
  <a>SPA PARTIES</a>
  <a>BOOTCAMP</a>
  <a>PRODUCTS</a>
  <a>ABOUT</a>
  <a style="border-right:0">CONTACT US</a>
</nav>

<section class="hero">
  <div class="hero-photo" role="img" aria-label="Photo of a laughing man wearing a grey clay face mask"></div>
  <h1>GLOWLAB</h1>
  <h2>SPECIALIST TREATMENTS</h2>
  <p>Lorem ipsum dolor sit amet, consectetur adipiscing elit, sed do eiusmod tempor incididunt ut labore</p>
  <a class="btn more">More Information</a>
  <div class="dots"><i class="on"></i><i></i><i></i><i></i></div>
</section>

<h2 class="sec-title" style="top:753px">OUR SERVICES</h2>

<article class="service" style="left:99px">
  <div class="pic" role="img" aria-label="Photo of a light therapy treatment"></div>
  <div class="shadow"></div>
  <h3>LIGHT THERAPY</h3>
  <p>Lorem ipsum dolor sit amet, sectetur adipiscing elit, sed do eiusmod tempor incididunt ut labore et dolore</p>
  <svg class="arrow" width="12" height="12" viewBox="0 0 12 12"><path d="M2 2l8 8M10 5v5H5" stroke="#aaa" fill="none" stroke-width="1.2"/></svg>
</article>
<article class="service" style="left:356px">
  <div class="pic" role="img" aria-label="Photo of an oxygen facial treatment"></div>
  <div class="shadow"></div>
  <h3>OXYGEN FACIAL</h3>
  <p>Lorem ipsum dolor sit amet, sectetur adipiscing elit, sed do eiusmod tempor incididunt ut labore et dolore</p>
  <svg class="arrow" width="12" height="12" viewBox="0 0 12 12"><path d="M2 2l8 8M10 5v5H5" stroke="#aaa" fill="none" stroke-width="1.2"/></svg>
</article>
<article class="service" style="left:613px">
  <div class="pic" role="img" aria-label="Photo of a microcurrent treatment"></div>
  <div class="shadow"></div>
  <h3>MICROCURRENT</h3>
  <p>Lorem ipsum dolor sit amet, sectetur adipiscing elit, sed do eiusmod tempor incididunt ut labore et dolore</p>
  <svg class="arrow" width="12" height="12" viewBox="0 0 12 12"><path d="M2 2l8 8M10 5v5H5" stroke="#aaa" fill="none" stroke-width="1.2"/></svg>
</article>
<article class="service" style="left:870px">
  <div class="pic" role="img" aria-label="Photo of a microdermabrasion treatment"></div>
  <div class="shadow"></div>
  <h3>MICRODERM</h3>
  <p>Lorem ipsum dolor sit amet, sectetur adipiscing elit, sed do eiusmod tempor incididunt ut labore et dolore</p>
  <svg class="arrow" width="12" height="12" viewBox="0 0 12 12"><path d="M2 2l8 8M10 5v5H5" stroke="#aaa" fill="none" stroke-width="1.2"/></svg>
</article>

<section class="welcome" role="img" aria-label="Teal band over a faint photo of a facial treatment">
  <h2>WELCOME TO GLOWLAB</h2>
  <p style="top:150px">GlowLab was born after it's founder Dana Merrow, a busy mom of 3 decided after her last facial that she is tired of wasting hours of her day and paying exorbitant prices to have products smeared on her face with no real visible results. "I remember lying on the table having my Esthetician trying to sell me everything under the sun while smearing products on my skin (which looked great when I walked out but absolutely no difference in my skin even after</p>
  <p style="top:222px">regular once a month facials," quoted Dana Merrow. So for us we believe the tradition of lying in a dark room for hours is a thing of the past. We created an open facial bar offering treatments that achieve incredible outcomes. We are not like other facial spas. We offer fresh hand made products on our spa bar along with medical style services. At GlowLab we believe beautiful skin begins with taking care of the largest organ</p>
</section>

<h2 class="sec-title" style="top:1620px">MEMBERSHIP OFFER</h2>

<article class="plan" style="left:120px">
  <div class="top"><div class="name">MEMBERSHIP1</div><div class="price"><sup>$</sup>600<small>.00 Per Month</small></div></div>
  <ul><li>Sed ut perspiciatis unde omnis</li><li>Nemo enim ipsam voluptatem quia</li><li>sed quia non numquam eius</li></ul>
  <a class="btn read">Read More</a>
</article>
<article class="plan" style="left:446px">
  <div class="top"><div class="name">MEMBERSHIP2</div><div class="price"><sup>$</sup>600<small>.00 Per Month</small></div></div>
  <ul><li>Sed ut perspiciatis unde omnis</li><li>Nemo enim ipsam voluptatem quia</li><li>sed quia non numquam eius</li></ul>
  <a class="btn read">Read More</a>
</article>
<article class="plan" style="left:771px">
  <div class="top"><div class="name">MEMBERSHIP3</div><div class="price"><sup>$</sup>600<small>.00 Per Month</small></div></div>
  <ul><li>Sed ut perspiciatis unde omnis</li><li>Nemo enim ipsam voluptatem quia</li><li>sed quia non numquam eius</li></ul>
  <a class="btn read">Read More</a>
</article>

<section class="testimonial">
  <h2>TESTIMONIAL</h2>
  <div class="avatar" role="img" aria-label="Portrait photo of a smiling client"></div>
  <p class="quote">" Nemo enim ipsam voluptatem quia voluptas sit aspernatur aut odit aut fugit, sed quia consequuntur magni dolores eos qui ratione voluptatem sequi nesciunt. Neque porro quisquam est, qui dolorem ipsum quia dolor sit amet, consectetur, adipisci velit, sed quia non numquam eius</p>
  <div class="author">Alex Reed- GlowLab</div>
  <div class="arrows">
    <svg width="14" height="14" viewBox="0 0 14 14"><circle cx="7" cy="7" r="7" fill="#fff"/><path d="M8.5 4L5.5 7l3 3" stroke="#14c5d4" stroke-width="1.6" fill="none"/></svg>
    <svg width="14" height="14" viewBox="0 0 14 14"><circle cx="7" cy="7" r="7" fill="#fff"/><path d="M5.5 4l3 3-3 3" stroke="#14c5d4" stroke-width="1.6" fill="none"/></svg>
  </div>
</section>

<footer class="footer">
  <div class="brand">glowlab</div>
  <div class="social"><i></i><i></i><i></i><i></i><i></i></div>

  <h4 style="left:371px">QUICK LINKS</h4>
  <ul class="links"><li>HOME</li><li>FACIAL MENU</li><li>SPA PARTIES</li><li>BOOTCAMP</li><li>PRODUCTS</li><li>CONTACT US</li></ul>

  <h4 style="left:586px">SIGN UP FOR NEWSLETTER</h4>
  <p class="news-text">Excepteur sint occaecat cupidatat non proident, sunt in culpa qui officia deserunt</p>
  <div class="field" style="top:117px">Enter Name</div>
  <div class="field" style="top:167px">Enter Email</div>
  <div class="subscribe">SUBSCRIBE</div>

  <h4 style="left:936px">CONTACT US</h4>
  <p class="contact">GlowLab<br>PO Box 100, Lakeview</p>
  <div class="contact-row" style="top:127px">
    <svg width="18" height="18" viewBox="0 0 24 24"><path d="M6.6 10.8a15 15 0 0 0 6.6 6.6l2.2-2.2c.3-.3.7-.4 1-.2 1.1.4 2.3.6 3.6.6.6 0 1 .4 1 1V20c0 .6-.4 1-1 1A17 17 0 0 1 3 4c0-.6.4-1 1-1h3.5c.6 0 1 .4 1 1 0 1.3.2 2.5.6 3.6.1.3 0 .7-.2 1z" fill="none" stroke="#888" stroke-width="1.5"/></svg>
    <span>+1 555 019 3348</span>
  </div>
  <div class="contact-row" style="top:156px">
    <svg width="18" height="14" viewBox="0 0 18 14"><rect x=".75" y=".75" width="16.5" height="12.5" fill="none" stroke="#888" stroke-width="1.3"/><path d="M1 1l8 6 8-6" fill="none" stroke="#888" stroke-width="1.3"/></svg>
    <span style="font-size:13px">hello@glowlab.example</span>
  </div>
</footer>

<div class="bottom">©2015 - 2016 &nbsp;GLOWLAB. All Rights Reserved.</div>

</body>
</html>
```